Your Ridgeview Homefinder Website Design

Creative Brief: Website Design for Your Ridgeview Homefinder
- Project Overview: Design a website for our new brand, "Your Ridgeview Homefinder". Your Ridgeview Homefinder is a service that matches clients with the perfect realtor. The primary function of this site is to serve as a lead generation hub, to generate leads of people who are looking to either buy or sell their house and need a great realtor. The site needs to have a very clean, modern design using sites like Quillmark, Lumhaven, Trevista, and Pravlo as an example. The site also needs to have a primary lead capture capability through a multi-step form or questionnaire that indicates if they are buying or selling, and depending on that selection, creates two different flows.

Target Audience:
- Homebuyers and sellers in the Denver area
- Individuals looking for high-quality realtor services
- Users seeking a seamless and professional online & home buying/selling experience

Objectives:
- Create a visually appealing, modern website with a strong emphasis on lead generation.
- Design advanced, multi-step forms for efficient lead capture.
- Ensure the website is user-friendly and optimized for both desktop and mobile devices.

Pages to Design:
Home Page:
- Engaging hero section with a clear call to action and the ability to enter the form flow
- Brief introduction to Your Ridgeview Homefinder and its unique value proposition
- Key features & benefits of being matched with a realtor by Your Ridgeview Homefinder
- Testimonials and success stories
- Lead capture form

About Page:
- Overview of Your Ridgeview Homefinder’s mission and values
- Professional and trust-building imagery

How it Works Page:
- Step-by-step explanation of the matching process (complete the form and we will match you with a realtor)
- Visual aids (icons, graphics) to simplify complex information
- Customer journey map from inquiry to successful match & sale of home
- Lead capture form

Contact Us Page:
- Simple and accessible contact form
- Contact details
- Call to action for immediate inquiries

Blog Template:
- Clean, easy-to-read layout for blog posts, primarily location/neighborhood guides as well as standard blogs
- Sidebar for recent posts, categories, and tags
- Social sharing buttons
- Lead capture form embedded within blog posts

Design Style:
- Modern and professional with a focus on usability
- Clean lines and intuitive navigation
- Use of curved corners and minimal straight lines for a sleek look
- Incorporation of graphic design elements, potentially including 3D and isomorphic design
- Inspired by sites like Quillmark, Lumhaven, Trevista, and Pravlo
Consistent color scheme and typography

Visual References:
- Quillmark: For its professional and corporate look
- Lumhaven and Trevista: For their user-friendly interfaces and modern design
- Pravlo: For its clean and functional layout

Target Market(s)

- Homebuyers and sellers in the Denver area, Individuals looking for high-quality realtor services, Users seeking a seamless and professional home buying/selling experience

Industry/Entity Type

Real Estate

Number of Pages Required

5+ page

Requirements
Must have
• Fully designed website with lead capture functionality based on brief
Nice to have
• Designed in Figma, Starting / Placeholder copy

```html
<!DOCTYPE html>
<html lang="en">
<head>
<meta charset="utf-8">
<title>Your Ridgeview Homefinder</title>
<link rel="stylesheet" href="https://fonts.googleapis.com/css2?family=Bebas+Neue&family=Montserrat:wght@300;400;500;600;700&display=swap">
<style>
:root{
  --orange:#f26430;
  --ink:#111111;
  --text:#2b2b2b;
  --light:#f3f3f3;
  --white:#ffffff;
  --star:#f5b301;
}
*{box-sizing:border-box;margin:0;padding:0}
html,body{width:1200px;height:5150px;overflow:hidden}
body{position:relative;font-family:"Montserrat",sans-serif;color:var(--text);background:var(--white)}
.abs{position:absolute}
.display{font-family:"Bebas Neue",sans-serif;font-weight:400;letter-spacing:.5px;white-space:nowrap}
.accent{color:var(--orange)}
.btn{position:absolute;display:flex;align-items:center;justify-content:center;font-weight:700;font-size:15px;text-transform:uppercase;color:var(--white);background:var(--orange);white-space:nowrap}
.btn.dark{background:var(--ink)}

/* top bar */
.topbar{left:0;top:0;width:1200px;height:34px;background:var(--ink);color:var(--white);font-size:13px}
.topbar .item{position:absolute;top:9px;display:flex;align-items:center;gap:8px}
.social{position:absolute;display:flex;gap:4px}
.social span{display:block;width:18px;height:18px;border:1.5px solid var(--white);border-radius:50%}

/* header */
.header{left:0;top:34px;width:1200px;height:86px;background:var(--white)}
.logo{position:absolute;left:74px;top:26px;font-size:34px;color:var(--orange)}
.nav{position:absolute;top:34px;font-size:12px;font-weight:500;color:var(--ink);text-transform:uppercase}
.nav a{position:absolute;white-space:nowrap;color:inherit;text-decoration:none}
.nav a.active{color:var(--orange)}
.nav a.active::after{content:"";position:absolute;left:-4px;right:-4px;top:28px;height:2px;background:var(--orange)}

/* hero */
.hero{left:0;top:120px;width:1200px;height:566px;background:var(--light)}
.hero-media{left:600px;top:160px;width:600px;height:526px;background:linear-gradient(135deg,#f3f3f3 0%,#e6e3e0 45%,#b9aaa0 70%,#5a5a5a 100%)}
.hero-kicker{left:76px;top:268px;font-size:22px;font-weight:500;color:var(--ink);white-space:nowrap}
.hero-title{left:76px;top:302px;font-size:56px;color:var(--orange)}
.hero-copy{left:76px;top:372px;width:500px;font-size:17px;line-height:30px;color:var(--text)}

/* lead form step 1 */
.leadform{left:150px;top:606px;width:900px;height:146px;background:var(--orange)}
.select{position:absolute;top:46px;height:52px;background:var(--white);font-size:13px;color:#444;display:flex;align-items:center;padding:0 22px;justify-content:space-between;white-space:nowrap}
.select::after{content:"";border:5px solid transparent;border-top:6px solid #333;margin-top:6px}

/* intro */
.intro-frame{left:196px;top:842px;width:354px;height:492px;background:var(--white);box-shadow:0 4px 20px rgba(0,0,0,.12)}
.intro-photo{left:208px;top:856px;width:332px;height:464px;background:linear-gradient(160deg,#d9dde3 0%,#5b6b86 45%,#1f2a44 75%,#e9e9e9 100%)}
.intro-video{left:78px;top:1090px;width:278px;height:176px;background:linear-gradient(135deg,#7c8a6d,#c2b9a4 50%,#8b8f95)}
.intro-kicker{left:612px;top:880px;font-size:48px;color:var(--orange)}
.intro-title{left:612px;top:940px;font-size:48px;color:var(--ink)}
.intro-copy{left:612px;top:1022px;width:494px;font-size:14.5px;line-height:30px;text-align:justify;color:var(--text)}

/* stats */
.stats{left:0;top:1432px;width:1200px;height:266px;background:var(--light)}
.stat{position:absolute;top:72px}
.stat .num{font-size:46px;font-weight:400;color:var(--orange);line-height:1;padding-bottom:10px;border-bottom:2px dotted #333;width:140px}
.stat .label{margin-top:22px;font-size:19px;font-weight:600;color:var(--ink);white-space:nowrap}

.section-title{position:absolute;left:0;width:1200px;text-align:center;font-size:64px;color:var(--ink)}

/* properties */
.tab{position:absolute;top:1924px;width:142px;height:52px;border:2px solid #333;display:flex;align-items:center;justify-content:center;font-size:17px;font-weight:500;color:var(--ink)}
.tab.active{background:var(--orange);border-color:var(--orange);color:var(--white);font-weight:700}
.card{position:absolute;top:2042px;width:312px;height:500px;background:var(--white);box-shadow:0 3px 18px rgba(0,0,0,.13)}
.card .photo{position:absolute;left:10px;top:10px;width:292px;height:258px}
.card .tag{position:absolute;left:26px;top:42px;padding:8px 12px;background:var(--orange);color:var(--white);font-size:17px;font-weight:600}
.card h3{position:absolute;left:28px;top:300px;font-size:25px;font-weight:600;color:var(--ink);white-space:nowrap}
.card .sub{position:absolute;left:28px;top:342px;font-size:14px}
.card .stars{position:absolute;left:28px;top:372px;color:var(--star);font-size:21px;letter-spacing:2px}
.card .price{position:absolute;left:28px;top:416px;font-size:26px;font-weight:700;color:var(--ink)}
.card .match{left:162px;top:412px;width:132px;height:44px;font-size:14px}
.arrow{position:absolute;width:48px;height:48px;border-radius:50%;display:flex;align-items:center;justify-content:center}
.arrow.outline{border:2px solid #333;background:var(--white)}
.arrow.filled{background:var(--orange)}

/* features */
.feature-ring{left:390px;top:2932px;width:440px;height:440px;border:2px solid #f6b59b;border-radius:50%}
.feature-photo{left:404px;top:2946px;width:412px;height:412px;border-radius:50%;background:radial-gradient(circle at 50% 45%,#ffffff 0%,#efeeec 60%,#d8d6d3 100%)}
.dot{position:absolute;width:14px;height:14px;border-radius:50%;background:var(--orange)}
.ficon{position:absolute;width:92px;height:92px;border-radius:50%;border:2px dashed #444;display:flex;align-items:center;justify-content:center}
.ficon .core{width:72px;height:72px;border-radius:50%;background:var(--orange);display:flex;align-items:center;justify-content:center}
.flabel{position:absolute;font-size:19px;font-weight:600;color:var(--ink);line-height:26px;white-space:nowrap}

/* testimonials */
.quote-mark{left:158px;top:3666px;font-family:"Bebas Neue",sans-serif;font-size:200px;line-height:1;color:var(--orange)}
.t-copy{left:252px;top:3700px;width:790px;font-size:14px;line-height:30px;text-align:justify;color:var(--text)}
.avatar{left:492px;top:3854px;width:60px;height:60px;border-radius:50%;background:linear-gradient(#d2d2d2,#8f9296)}
.t-name{left:572px;top:3866px;font-size:17px;font-weight:700;color:var(--orange)}
.t-role{left:572px;top:3894px;font-size:12px;color:var(--text)}
.pager{left:550px;top:3970px;display:flex;gap:12px;align-items:center}
.pager span{width:12px;height:12px;border-radius:50%;background:#cfcfcf}
.pager span.on{width:28px;height:6px;border-radius:3px;background:var(--orange)}

/* contact */
.contact{left:0;top:4084px;width:1200px;height:696px;background:linear-gradient(#f7f7f7,#ececec)}
.field{position:absolute;height:56px;background:var(--white);border-radius:4px;display:flex;align-items:center;gap:12px;padding:0 28px;font-size:14px;color:#777}
.field.area{align-items:flex-start;padding-top:20px;height:114px}

/* footer */
.footer{left:0;top:4780px;width:1200px;height:294px;background:var(--orange);color:var(--white)}
.f-title{position:absolute;left:0;top:52px;width:1200px;text-align:center;font-size:46px}
.f-item{position:absolute;top:140px;display:flex;gap:18px;align-items:center;font-size:12px;line-height:17px}
.f-item .ic{width:26px;height:26px;border-radius:4px;background:var(--white);display:flex;align-items:center;justify-content:center}
.f-rule{position:absolute;left:150px;top:222px;width:900px;height:1px;background:rgba(255,255,255,.45)}
.f-nav a{position:absolute;top:252px;font-size:13px;color:var(--white);text-decoration:none;white-space:nowrap}
.bottombar{left:0;top:5074px;width:1200px;height:76px;background:var(--ink);color:var(--white);font-size:12px}
.sq{display:block;width:26px;height:26px;background:var(--orange);border-radius:3px}
</style>
</head>
<body>

<div class="abs topbar">
  <div class="item" style="left:82px">
    <svg width="12" height="12" viewBox="0 0 24 24"><path fill="#f26430" d="M6.6 10.8a15 15 0 006.6 6.6l2.2-2.2a1 1 0 011-.25 11.4 11.4 0 003.6.57 1 1 0 011 1V20a1 1 0 01-1 1A17 17 0 013 4a1 1 0 011-1h3.5a1 1 0 011 1c0 1.25.2 2.45.57 3.57a1 1 0 01-.25 1z"/></svg>
    <span>555 014 2290</span>
  </div>
  <div class="item" style="left:228px">
    <svg width="14" height="11" viewBox="0 0 24 18"><rect width="24" height="18" rx="2" fill="#f26430"/><path d="M2 2l10 8 10-8" stroke="#111" stroke-width="2" fill="none"/></svg>
    <span>hello@ridgeviewhf.example</span>
  </div>
  <div class="social" style="left:1010px;top:8px"><span></span><span></span><span></span><span></span><span></span></div>
</div>

<header class="abs header">
  <div class="logo display">Your Ridgeview Homefinder</div>
  <nav class="nav">
    <a class="active" style="left:458px">Home</a>
    <a style="left:522px">About Us</a>
    <a style="left:614px">Features &amp; Benefits</a>
    <a style="left:772px">Testimonials</a>
    <a style="left:890px">Contact Us</a>
  </nav>
  <div class="btn" style="left:986px;top:24px;width:140px;height:38px;font-size:13px;font-weight:600">Get a Quote</div>
</header>

<section class="abs hero"></section>
<div class="abs hero-media" role="img" aria-label="Hand holding a small model of a modern two-storey house"></div>
<div class="abs hero-kicker">YOUR RIDGEVIEW HOMEFINDER</div>
<h1 class="abs hero-title display">Find Your Dream House By Us</h1>
<p class="abs hero-copy">Lorem ipsum dolor sit amet, consectetur adipiscing elit, sed do eiusmod tempor incididunt ut labore et dolore</p>
<div class="btn dark" style="left:76px;top:468px;width:192px;height:64px;font-size:15px;font-weight:600">Make an Enquiry</div>

<form class="abs leadform" aria-label="Step one of the matching questionnaire">
  <div class="select" style="left:30px;width:204px">Buying or Selling?</div>
  <div class="select" style="left:248px;width:202px">Choose Area</div>
  <div class="select" style="left:462px;width:202px">Property Type</div>
  <div class="btn dark" style="left:682px;top:40px;width:184px;height:60px;font-size:16px">Next Step</div>
</form>

<div class="abs intro-frame"></div>
<div class="abs intro-photo" role="img" aria-label="Realtor in a navy suit holding out house keys beside a model house"></div>
<div class="abs intro-video" role="img" aria-label="Video thumbnail of an architectural apartment model">
  <svg class="abs" style="left:111px;top:60px" width="56" height="56" viewBox="0 0 56 56"><circle cx="28" cy="28" r="25" fill="none" stroke="#fff" stroke-width="3"/><path d="M22 17l17 11-17 11z" fill="#fff"/></svg>
</div>
<div class="abs intro-kicker display">Introduction To</div>
<h2 class="abs intro-title display">Your Ridgeview Homefinder</h2>
<p class="abs intro-copy">Lorem ipsum dolor sit amet, consectetur adipiscing elit, sed do eius mod tempor incididunt ut labore et dolore magna aliqua. Ut enim ad minim veniam, quis nostrud exercitation ullamco laboris nisi ut aliquip ex ea commodo consequat. Lorem ipsum dolor sit amet, con sectetur adipiscing elit, sed do eius mod tempor incididunt ut labore et dolore magna aliqua. Ut enim ad minim veniam,.</p>
<div class="btn" style="left:614px;top:1236px;width:170px;height:58px;font-size:16px">Read More</div>

<section class="abs stats">
  <div class="stat" style="left:154px"><div class="num">560+</div><div class="label">Total Area Sq</div></div>
  <div class="stat" style="left:384px"><div class="num">197k+</div><div class="label">Apartments Sold</div></div>
  <div class="stat" style="left:628px"><div class="num">268+</div><div class="label">Total Constructions</div></div>
  <div class="stat" style="left:904px"><div class="num">330+</div><div class="label">Apartio Rooms</div></div>
</section>

<h2 class="section-title display" style="top:1806px"><span class="accent">Best Properties</span> Buying or Selling</h2>
<div class="tab active" style="left:366px">ALL</div>
<div class="tab" style="left:530px">BUYING</div>
<div class="tab" style="left:692px">FOR SALE</div>

<div class="arrow outline" style="left:50px;top:2276px"><svg width="18" height="14" viewBox="0 0 18 14"><path d="M17 7H2M7 1L1 7l6 6" stroke="#111" stroke-width="2" fill="none"/></svg></div>
<div class="arrow filled" style="left:1104px;top:2276px"><svg width="18" height="14" viewBox="0 0 18 14"><path d="M1 7h15M11 1l6 6-6 6" stroke="#fff" stroke-width="2" fill="none"/></svg></div>

<article class="card" style="left:116px">
  <div class="photo" role="img" aria-label="White modern villa with a swimming pool" style="background:linear-gradient(#cfe3f5 0%,#eaeaea 45%,#6f6a62 65%,#2a6f9a 80%,#1d4f78 100%)"></div>
  <h3>Best Property One</h3><div class="sub">Lorem ipsum dolor sit amet</div>
  <div class="stars">★★★★★</div><div class="price">$95,000</div>
  <div class="btn match">Get Matched</div>
</article>
<article class="card" style="left:444px">
  <div class="photo" role="img" aria-label="Tall yellow apartment tower under blue sky" style="background:linear-gradient(#9ec7ec 0%,#cdb77a 40%,#b9a36a 70%,#6f8f4a 100%)"></div>
  <div class="tag">FOR SALE</div>
  <h3>Best Property Two</h3><div class="sub">Lorem ipsum dolor sit amet</div>
  <div class="stars">★★★★★</div><div class="price">$95,000</div>
</article>
<article class="card" style="left:772px">
  <div class="photo" role="img" aria-label="Modern dark apartment blocks with trees" style="background:linear-gradient(#d5e4f2 0%,#5e6265 40%,#3b3f42 70%,#7d8c5d 100%)"></div>
  <h3>Best Property Three</h3><div class="sub">Lorem ipsum dolor sit amet</div>
  <div class="stars">★★★★★</div><div class="price">$95,000</div>
  <div class="btn match">Get Matched</div>
</article>

<h2 class="section-title display" style="top:2694px"><span class="accent">Key Features</span> &amp; Benefits</h2>
<div class="abs feature-ring"></div>
<div class="abs feature-photo" role="img" aria-label="Woman in white shirt holding a small model house and keys"></div>
<span class="dot" style="left:513px;top:2937px"></span>
<span class="dot" style="left:673px;top:2937px"></span>
<span class="dot" style="left:409px;top:3049px"></span>
<span class="dot" style="left:825px;top:3049px"></span>
<span class="dot" style="left:401px;top:3235px"></span>
<span class="dot" style="left:823px;top:3235px"></span>
<span class="dot" style="left:513px;top:3343px"></span>
<span class="dot" style="left:719px;top:3343px"></span>

<div class="ficon" style="left:446px;top:2838px"><div class="core"><svg width="34" height="34" viewBox="0 0 24 24" fill="none" stroke="#fff" stroke-width="1.6"><circle cx="11" cy="10" r="3"/><path d="M5 20c0-3 3-5 6-5s6 2 6 5"/><circle cx="18" cy="17" r="3"/><path d="M16.8 17l1 1 1.6-1.8"/></svg></div></div>
<div class="ficon" style="left:706px;top:2838px"><div class="core"><svg width="34" height="34" viewBox="0 0 24 24" fill="none" stroke="#fff" stroke-width="1.6"><path d="M4 20V14M8 20V10M12 20V6"/><circle cx="17" cy="15" r="4"/><path d="M17 13v4"/></svg></div></div>
<div class="ficon" style="left:306px;top:2990px"><div class="core"><svg width="34" height="34" viewBox="0 0 24 24" fill="none" stroke="#fff" stroke-width="1.6"><path d="M3 11l9-7 9 7M5 10v10h14V10"/><path d="M9 13l6 5M15 13l-6 5"/></svg></div></div>
<div class="ficon" style="left:846px;top:2994px"><div class="core"><svg width="34" height="34" viewBox="0 0 24 24" fill="none" stroke="#fff" stroke-width="1.6"><rect x="5" y="3" width="14" height="18" rx="1"/><path d="M8 8h8M8 12h8M8 16h5"/></svg></div></div>
<div class="ficon" style="left:294px;top:3184px"><div class="core"><svg width="36" height="34" viewBox="0 0 24 24" fill="none" stroke="#fff" stroke-width="1.6"><circle cx="12" cy="8" r="3"/><circle cx="5" cy="10" r="2"/><circle cx="19" cy="10" r="2"/><path d="M7 19c0-3 2-5 5-5s5 2 5 5M2 18c0-2 1-4 3-4M22 18c0-2-1-4-3-4"/></svg></div></div>
<div class="ficon" style="left:856px;top:3190px"><div class="core"><svg width="34" height="34" viewBox="0 0 24 24" fill="none" stroke="#fff" stroke-width="1.6"><rect x="3" y="4" width="18" height="12" rx="1"/><path d="M9 20h6M12 16v4M10 8l-2 2 2 2M14 8l2 2-2 2"/></svg></div></div>
<div class="ficon" style="left:446px;top:3374px"><div class="core"><svg width="34" height="34" viewBox="0 0 24 24" fill="none" stroke="#fff" stroke-width="1.6"><path d="M3 11l9-7 9 7M5 10v10h14V10"/><rect x="10" y="14" width="4" height="6"/></svg></div></div>
<div class="ficon" style="left:706px;top:3374px"><div class="core"><svg width="34" height="34" viewBox="0 0 24 24" fill="none" stroke="#fff" stroke-width="1.6"><rect x="6" y="3" width="12" height="17" rx="1"/><path d="M9 8h6M9 12h6M9 16h4"/></svg></div></div>

<div class="flabel" style="left:272px;top:2866px">Pricing Expertise</div>
<div class="flabel" style="left:828px;top:2866px">Avoiding Closing Problems</div>
<div class="flabel" style="left:110px;top:3024px">Requesting Repairs</div>
<div class="flabel" style="left:964px;top:3014px">Thorough Record<br>Keeping</div>
<div class="flabel" style="left:76px;top:3220px">Ethical Consideration</div>
<div class="flabel" style="left:972px;top:3222px">Code Expertise</div>
<div class="flabel" style="left:200px;top:3412px">Finding Available Homes</div>
<div class="flabel" style="left:816px;top:3408px">Tackling the Paperwork</div>

<h2 class="section-title display" style="top:3600px"><span class="accent">Our</span> Testimonials</h2>
<div class="abs quote-mark">“</div>
<p class="abs t-copy">Lorem ipsum dolor sit amet, conse ctetuer adipiscing elit. Aenean comodo ligula eget dolor. Aenean massa. Cum sociis na toque pen atibus et magnis dis parturient montes, nascetur ridiculus mus. Donec quam felis, ultricies nec, pellentesque eu, pretium quis, sem. Nulla consequat massa quis enim. Donec pede justo, fringilla vel, aliquet nec, vulputate eget, arcu. In enim justo, rhoncus ut, imperdiet a, venenatis vitae, justo. Nullam dictum felis eu pede mollis pretium. Integer tincidunt. Cras dapibus. Vivamus elementum</p>
<div class="abs avatar" role="img" aria-label="Client portrait"></div>
<div class="abs t-name">Marcus Ellery</div>
<div class="abs t-role">Managing Director</div>
<div class="abs pager"><span class="on"></span><span></span><span></span><span></span></div>
<div class="arrow outline" style="left:50px;top:3762px"><svg width="18" height="14" viewBox="0 0 18 14"><path d="M17 7H2M7 1L1 7l6 6" stroke="#111" stroke-width="2" fill="none"/></svg></div>
<div class="arrow filled" style="left:1104px;top:3762px"><svg width="18" height="14" viewBox="0 0 18 14"><path d="M1 7h15M11 1l6 6-6 6" stroke="#fff" stroke-width="2" fill="none"/></svg></div>

<section class="abs contact" role="img" aria-label="Faint city skyline backdrop"></section>
<h2 class="section-title display" style="top:4176px"><span class="accent">Contact</span> Us</h2>
<div class="field" style="left:224px;top:4298px;width:370px"><svg width="12" height="12" viewBox="0 0 24 24" fill="#999"><circle cx="12" cy="7" r="5"/><path d="M2 24c0-6 4-9 10-9s10 3 10 9z"/></svg>First Name</div>
<div class="field" style="left:604px;top:4298px;width:370px"><svg width="14" height="10" viewBox="0 0 24 18"><rect width="24" height="18" rx="2" fill="#999"/><path d="M2 2l10 8 10-8" stroke="#fff" stroke-width="2" fill="none"/></svg>E-Mail</div>
<div class="field" style="left:224px;top:4382px;width:370px"><svg width="9" height="13" viewBox="0 0 12 20" fill="none" stroke="#999" stroke-width="2"><rect x="1" y="1" width="10" height="18" rx="2"/></svg>Phone Number</div>
<div class="field" style="left:604px;top:4382px;width:370px"><svg width="10" height="13" viewBox="0 0 20 26" fill="#999"><path d="M10 0a10 10 0 00-10 10c0 7 10 16 10 16s10-9 10-16A10 10 0 0010 0zm0 14a4 4 0 110-8 4 4 0 010 8z"/></svg>Address</div>
<div class="field area" style="left:224px;top:4466px;width:750px"><svg width="12" height="12" viewBox="0 0 24 24" fill="#999"><circle cx="12" cy="12" r="11"/></svg>Message</div>
<div class="btn" style="left:504px;top:4624px;width:190px;height:54px;font-size:15px">Submit Now</div>

<footer class="abs footer">
  <div class="f-title display">Your Ridgeview Homefinder</div>
  <div class="f-item" style="left:214px"><span class="ic"><svg width="14" height="14" viewBox="0 0 24 24"><path fill="#f26430" d="M6.6 10.8a15 15 0 006.6 6.6l2.2-2.2a1 1 0 011-.25 11.4 11.4 0 003.6.57 1 1 0 011 1V20a1 1 0 01-1 1A17 17 0 013 4a1 1 0 011-1h3.5a1 1 0 011 1c0 1.25.2 2.45.57 3.57a1 1 0 01-.25 1z"/></svg></span><div>CALL US<br>555 014 7731</div></div>
  <div class="f-item" style="left:432px"><span class="ic"><svg width="14" height="11" viewBox="0 0 24 18"><rect width="24" height="18" rx="2" fill="#f26430"/><path d="M2 2l10 8 10-8" stroke="#fff" stroke-width="2" fill="none"/></svg></span><div>EMAIL US<br>hello@ridgeviewhf.example</div></div>
  <div class="f-item" style="left:746px"><span class="ic"><svg width="11" height="14" viewBox="0 0 20 26" fill="#f26430"><path d="M10 0a10 10 0 00-10 10c0 7 10 16 10 16s10-9 10-16A10 10 0 0010 0zm0 14a4 4 0 110-8 4 4 0 010 8z"/></svg></span><div>Address line Dummy Here<br>Address line Here</div></div>
  <div class="f-rule"></div>
  <nav class="f-nav">
    <a style="left:296px">HOME</a>
    <a style="left:382px">ABOUT US</a>
    <a style="left:494px">FEATURES &amp; BENEFITS</a>
    <a style="left:678px">TESTIMONIALS</a>
    <a style="left:820px">CONTACT US</a>
  </nav>
</footer>
<div class="abs bottombar">
  <div class="abs" style="left:76px;top:30px">Copyright © 2024 All Rights Reserved By Company name</div>
  <div class="social" style="left:992px;top:24px;gap:10px"><i class="sq"></i><i class="sq"></i><i class="sq"></i><i class="sq"></i></div>
</div>

</body>
</html>
```